Contemporary new French wine brand needs logo and series of label design

to design a new contemporary logo and series of labels for a new French wine brand. We hope to attract not just current French wine drinkers but new ones who may appreciate a less traditional and more modern style.
Updates

Reason: we are wanting to extend the project for a few days more to receive more submissions since we had fewer designs submitted than we were expecting, maybe because of the holidays.

Target Market(s)

people who follow the arts community (eg. music, theatre, visual/video arts, dance) --- all mature ages.

Industry/Entity Type

French Wine

Requirements
Must have
• a clear, memorable treatment for the name CLAVINE with accompanying logo.
Nice to have
• embossing, matte/gloss refinement, tasteful foil stamping, coated stock for the whites to help the integrity of the paper in and out of ice buckets. A combo of say, three types of fonts; a semi custom font for the brand name Clavine and maybe a script and one other.
Should not have
• not traditional French

```html
<!DOCTYPE html>
<html lang="en">
<head>
<meta charset="UTF-8">
<title>Clavine — Cabernet Sauvignon Label</title>
<link href="https://fonts.googleapis.com/css2?family=Josefin+Sans:wght@300&family=Fira+Mono&family=Petit+Formal+Script&display=swap" rel="stylesheet">
<style>
  :root {
    --page: #ffffff;
    --label: #000000;
    --frame-light: #e9c9a0;
    --frame-mid: #b06a35;
    --frame-dark: #5a1e10;
    --copper: rgba(201, 138, 88, 0.5);
    --rust: rgba(138, 58, 20, 0.6);
    --wine: rgba(90, 16, 16, 0.75);
    --clear: rgba(0, 0, 0, 0);
    --title: #ffffff;
    --muted: #3b3b3b;
  }
  * { margin: 0; padding: 0; box-sizing: border-box; }
  html, body {
    width: 1200px;
    height: 1200px;
    overflow: hidden;
    background: var(--page);
  }
  .canvas {
    position: relative;
    width: 1200px;
    height: 1200px;
  }
  .label {
    position: absolute;
    left: 208px;
    top: 146px;
    width: 784px;
    height: 872px;
    background: var(--label);
    overflow: hidden;
  }
  .label__frame {
    position: absolute;
    left: 13px;
    top: 13px;
    width: 758px;
    height: 846px;
  }
  .label__ornament {
    position: absolute;
    left: 30px;
    top: 50px;
    width: 724px;
    height: 440px;
    background:
      radial-gradient(ellipse 190px 110px at 52% 28%, var(--copper), var(--clear)),
      radial-gradient(ellipse 110px 90px at 26% 30%, var(--rust), var(--clear)),
      radial-gradient(ellipse 90px 170px at 9% 55%, var(--wine), var(--clear)),
      radial-gradient(ellipse 80px 130px at 92% 52%, var(--wine), var(--clear)),
      radial-gradient(ellipse 110px 150px at 74% 78%, var(--rust), var(--clear)),
      radial-gradient(ellipse 70px 60px at 25% 72%, var(--rust), var(--clear));
  }
  .label__brand {
    position: absolute;
    left: 0;
    width: 100%;
    top: 226px;
    text-align: center;
    font-family: "Josefin Sans", sans-serif;
    font-weight: 300;
    font-size: 92px;
    line-height: 1;
    letter-spacing: 0.3em;
    padding-left: 0.3em;
    color: var(--title);
  }
  .label__info {
    position: absolute;
    left: 0;
    width: 100%;
    text-align: center;
    font-family: "Fira Mono", monospace;
    font-size: 35px;
    letter-spacing: 0.08em;
    color: var(--muted);
    line-height: 1;
  }
  .label__vintage { top: 570px; }
  .label__region { top: 628px; }
  .label__country { top: 806px; }
  .label__varietal {
    position: absolute;
    left: 0;
    width: 100%;
    top: 700px;
    text-align: center;
    font-family: "Petit Formal Script", cursive;
    font-size: 50px;
    line-height: 1.2;
    color: var(--title);
  }
</style>
</head>
<body>
<div class="canvas">
  <div class="label">
    <svg class="label__frame" viewBox="0 0 758 846" aria-hidden="true">
      <defs>
        <linearGradient id="frameGradient" x1="0" y1="0" x2="1" y2="1">
          <stop offset="0" stop-color="#e9c9a0"/>
          <stop offset="0.5" stop-color="#b06a35"/>
          <stop offset="0.8" stop-color="#5a1e10"/>
          <stop offset="1" stop-color="#e9c9a0"/>
        </linearGradient>
      </defs>
      <rect x="1.5" y="1.5" width="755" height="843" fill="none" stroke="url(#frameGradient)" stroke-width="3"/>
    </svg>
    <div class="label__ornament" role="img" aria-label="Copper and wine-red flourished swirl ornament framing the brand name"></div>
    <h1 class="label__brand">CLAVINE</h1>
    <p class="label__info label__vintage">2016</p>
    <p class="label__info label__region">LOCATION VALLEY</p>
    <p class="label__varietal">Cabernet Sauvignon</p>
    <p class="label__info label__country">FRANCE</p>
  </div>
</div>
</body>
</html>
```